Vintage home page design (Bellweather Coupes and Wagons - 7815)

Wants a vintage-themed website.
http://www.bellweathercoupeshub.com/
Likes the retro graphics used on this site (the signs and the cartoon at the bottom of the boy holding the flag)

Client is open to a light or dark background, and wants to see what you come up with. Use their logo colors as accent colors throughout the home page design.
Keep it retro and vintage and have fun!

Attached their logo and a .psd layout example. The layout example is just for referencing the dimensions we usually use, but it's not set in stone.

Let me know if you have any questions and I'll answer them as soon as possible.

Thank you designers for your early submissions! I am waiting to hear back from the client and will keep each of you updated when they reply. Best regards, Maribel

Hello everyone- Thanks so much for being patient, I am still waiting to hear back from the client and get feedback. I just sent another follow up email and will let you all know when I get feedback. Best regards, Maribel

```html
<!DOCTYPE html>
<html lang="en">
<head>
<meta charset="utf-8">
<title>Bellweather Coupes and Wagons</title>
<link rel="stylesheet" href="https://fonts.googleapis.com/css2?family=Fredoka:wght@500;600&family=Enriqueta:wght@400;700&family=Open+Sans:wght@400;600&display=swap">
<style>
:root{
  --navy:#1b2a8c;
  --navy-dark:#0e1a6b;
  --royal:#2b3fb5;
  --red:#e0202c;
  --red-dark:#b80f1a;
  --cream:#fbf7b0;
  --cream-soft:#f7f4c2;
  --maroon:#8a0f12;
  --ink:#2a2a2a;
  --grey:#666;
  --gold:#f5e27a;
  --white:#fff;
}
*{box-sizing:border-box;margin:0;padding:0}
html,body{width:908px;height:1200px;overflow:hidden;background:var(--white)}
.page{position:relative;width:908px;height:1200px;overflow:hidden;font-family:"Open Sans",sans-serif;color:var(--ink)}
.backdrop{position:absolute;left:0;top:0;width:908px;height:560px}
.header-sky{position:absolute;left:0;top:0;width:908px;height:160px;
  background:radial-gradient(ellipse at 50% 40%,#3a55d6 0%,#2238b0 35%,#14238a 75%,#0d1870 100%)}
.zigzag-top{position:absolute;left:0;top:0;width:908px;height:9px}
.brand{position:absolute;left:374px;top:30px;width:160px;text-align:center;
  font-family:"Fredoka",sans-serif;font-weight:600;font-size:15px;line-height:17px;color:var(--gold)}
.brand-dot{display:block;width:14px;height:14px;border-radius:50%;background:var(--red);margin:0 auto 6px}
.main-nav{position:absolute;left:72px;top:115px;width:770px;height:48px;
  background:linear-gradient(#2136a8,#1a2a90);display:flex;align-items:center;justify-content:space-between;padding:0 26px}
.nav-group{display:flex;align-items:center;gap:14px;list-style:none}
.nav-group a{font-family:"Fredoka",sans-serif;font-weight:500;font-size:13.5px;color:#fff8d0;text-decoration:none;letter-spacing:.2px}
.nav-star{color:var(--gold);font-size:12px}
.hero{position:absolute;left:70px;top:163px;width:768px;height:296px;
  background:linear-gradient(180deg,#e9e9ec 0%,#d2d3d8 45%,#9d9fa5 75%,#5e6066 100%)}
.hero-arrow{position:absolute;top:130px}
.hero-caption{position:absolute;left:70px;top:459px;width:768px;height:82px;background:var(--cream);
  clip-path:polygon(0 0,100% 0,100% 92%,50% 100%,0 96%)}
.hero-title{position:absolute;left:30px;top:20px;font-family:"Fredoka",sans-serif;font-weight:500;font-size:16.5px;color:var(--maroon)}
.hero-sub{position:absolute;left:30px;top:44px;font-size:10px;color:#b8b37a}
.btn{display:inline-flex;align-items:center;justify-content:center;gap:5px;background:linear-gradient(#2a3ca8,#18258a);
  color:#fff;font-family:"Fredoka",sans-serif;font-weight:500;font-size:10.5px;text-decoration:none;letter-spacing:.2px}
.hero-caption .btn{position:absolute;left:623px;top:20px;width:102px;height:29px}
.welcome{position:absolute;left:70px;top:578px;width:530px}
.welcome h1{font-family:"Enriqueta",serif;font-weight:400;font-size:19px;letter-spacing:.6px;color:var(--ink)}
.welcome .lead{margin:10px 0 0 4px;font-size:11.6px;line-height:16.5px;color:var(--grey)}
.welcome .body{margin:10px 0 0 4px;font-size:9.8px;line-height:16.5px;color:#6f6f6f}
.contact-card{position:absolute;left:625px;top:570px;width:214px;height:160px;
  background:linear-gradient(#e71d28,#c50c16);color:#fff;text-align:center;border-radius:2px}
.contact-card h2{margin-top:20px;font-family:"Fredoka",sans-serif;font-weight:500;font-size:19px;display:flex;justify-content:center;align-items:center;gap:12px}
.contact-card h2 span{color:#ff8a8f;font-size:11px}
.contact-card p{margin-top:14px;font-size:10.3px;line-height:16.5px}
.contact-card .phone{margin-top:1px;font-size:14.5px}
.divider{position:absolute;left:70px;top:766px;width:766px;height:3px;
  background:radial-gradient(circle,#c9c9c9 1.3px,transparent 1.6px) 0 0/5.4px 3px repeat-x}
.featured-title{position:absolute;left:70px;top:802px;font-family:"Enriqueta",serif;font-weight:400;font-size:19px;color:var(--red);letter-spacing:.4px}
.vehicles{position:absolute;left:69px;top:837px;display:flex;gap:8px;list-style:none}
.vehicle{width:188px;text-align:center}
.vehicle-photo{height:103px;border:3px solid #fff;box-shadow:0 0 0 1px #ddd}
.vehicle h3{margin-top:15px;font-family:"Fredoka",sans-serif;font-weight:500;font-size:12.5px;color:var(--navy)}
.vehicle p{margin-top:4px;font-size:9.7px;line-height:16.5px;color:var(--grey)}
.vehicle .btn{margin-top:10px;width:102px;height:29px}
.vehicle .btn span{color:#a9b2e8;font-size:8px}
.footer{position:absolute;left:0;top:1090px;width:908px;height:110px;background:var(--cream-soft)}
.footer-zig{position:absolute;left:0;top:-9px;width:908px;height:10px}
.footer-nav{position:absolute;left:72px;top:38px;display:flex;list-style:none;font-family:"Enriqueta",serif;font-size:11.5px}
.footer-nav li+li:before{content:"|";margin:0 5px;color:var(--ink)}
.footer-nav a{color:var(--ink);text-decoration:none;letter-spacing:.3px}
.copyright{position:absolute;left:72px;top:61px;font-size:9.5px;color:#555}
.social{position:absolute;left:764px;top:44px;display:flex;gap:8px;list-style:none}
.social li{width:18px;height:18px;border-radius:50%;background:var(--red-dark)}
</style>
</head>
<body>
<div class="page">
  <svg class="backdrop" viewBox="0 0 908 560" aria-hidden="true">
    <path d="M0 128H58V480Q20 496 0 512Z" fill="#e3202d"/>
    <path d="M0 470Q40 460 70 452V480Q30 490 0 500Z" fill="#f6a0a4"/>
    <path d="M850 128H908V530Q870 440 838 410V128Z" fill="#e3202d"/>
    <path d="M838 380Q890 420 908 470V540Q880 470 838 440Z" fill="#f28d93"/>
    <path d="M840 180L838 485" stroke="#a10d16" stroke-width="4"/>
  </svg>
  <div class="header-sky"></div>
  <svg class="zigzag-top" viewBox="0 0 908 9" preserveAspectRatio="none" aria-hidden="true">
    <defs><pattern id="zigTop" width="12" height="9" patternUnits="userSpaceOnUse"><path d="M0 0H12L6 7Z" fill="#f4ef9a"/></pattern></defs>
    <rect width="908" height="9" fill="url(#zigTop)"/>
  </svg>
  <svg style="position:absolute;left:40px;top:100px" width="828" height="50" viewBox="0 0 828 50" aria-hidden="true">
    <path d="M10 0H70L80 48H0L12 26Z" fill="#1f35a6"/>
    <path d="M818 0H758L748 48H828L816 26Z" fill="#1f35a6"/>
  </svg>

  <nav class="main-nav">
    <ul class="nav-group">
      <li><a href="#">HOME</a></li><li class="nav-star">★</li>
      <li><a href="#">ABOUT US</a></li><li class="nav-star">★</li>
      <li><a href="#">SELL YOUR CLASSIC</a></li>
    </ul>
    <ul class="nav-group">
      <li><a href="#">INVENTORY</a></li><li class="nav-star">★</li>
      <li><a href="#">CONTACT</a></li><li class="nav-star">★</li>
      <li><a href="#">VIP LIST</a></li>
    </ul>
  </nav>
  <div class="brand"><span class="brand-dot"></span>Bellweather Coupes and Wagons</div>

  <div class="hero" role="img" aria-label="Photo of a silver 1950s hardtop coupe on a checkered showroom floor">
    <svg class="hero-arrow" style="left:14px" width="22" height="40" viewBox="0 0 22 40" aria-hidden="true"><path d="M20 2L3 20L20 38" fill="none" stroke="#fff" stroke-width="2.5"/></svg>
    <svg class="hero-arrow" style="right:14px" width="22" height="40" viewBox="0 0 22 40" aria-hidden="true"><path d="M2 2L19 20L2 38" fill="none" stroke="#fff" stroke-width="2.5"/></svg>
  </div>
  <div class="hero-caption">
    <h2 class="hero-title">Phasellus felis dolor scelerisque tempus eget</h2>
    <p class="hero-sub">Mauris vel lacus vitae felis vestibulum volutpat Etiam est nunc venenatis in tristique</p>
    <a class="btn" href="#">READ MORE</a>
  </div>

  <section class="welcome">
    <h1>WELCOME TO OUR WEBSITE MAINPAGE</h1>
    <p class="lead">Mauris vel lacus vitae felis vestibulum volutpat Etiam est nunc venenatis in tristique eu imperdiet ac nisl Cum sociis natoque penatibus et magnis dis parturient montes</p>
    <p class="body">Vivamus porttitor g purus nisi eleifend libero a tempus libero lectus feugiat felis Morbi diam mauris viverra in gravida eu mattis in ante Morbi eget arcu Morbi porta libero id ullamcorper nonummy nibh ligula pulvinar metus eget consectetuer augue nisi quis lacus Ut ac mi quis lacus mollis aliquam Curabitur iaculis tempus eros Curabitur vel mi sit amet magna malesuada ultrices Ut nisi erat fermentum vel congue id euismod in elit Fusce ultricies</p>
  </section>

  <aside class="contact-card">
    <h2><span>★</span>CONTACT US<span>★</span></h2>
    <p>Northgate Classic Motors<br>Larkspur District Fairview,<br>Colorado 80917</p>
    <p class="phone">555-013-2710</p>
  </aside>

  <div class="divider"></div>

  <h2 class="featured-title">FEATURED VEHICLE</h2>
  <ul class="vehicles">
    <li class="vehicle">
      <div class="vehicle-photo" role="img" aria-label="Red classic hardtop in a white studio" style="background:linear-gradient(#f4f4f4 0%,#e6e6e6 60%,#c43a34 72%,#9c2a26 86%,#3a3a3a 100%)"></div>
      <h3>VEHICLE NAME</h3>
      <p>Arta libero id ullamcorper nonummy<br>nibh ligula pulvinar metus eget</p>
      <a class="btn" href="#"><span>★</span>READ MORE<span>★</span></a>
    </li>
    <li class="vehicle">
      <div class="vehicle-photo" role="img" aria-label="White classic sedan in a white studio" style="background:linear-gradient(#f4f4f4 0%,#e8e8e8 60%,#efece4 74%,#c9c6bd 88%,#3a3a3a 100%)"></div>
      <h3>VEHICLE NAME</h3>
      <p>Arta libero id ullamcorper nonummy<br>nibh ligula pulvinar metus eget</p>
      <a class="btn" href="#"><span>★</span>READ MORE<span>★</span></a>
    </li>
    <li class="vehicle">
      <div class="vehicle-photo" role="img" aria-label="Light blue classic hardtop in a white studio" style="background:linear-gradient(#f4f4f4 0%,#e6e6e6 58%,#8fa3d4 72%,#6d82bb 86%,#3a3a3a 100%)"></div>
      <h3>VEHICLE NAME</h3>
      <p>Arta libero id ullamcorper nonummy<br>nibh ligula pulvinar metus eget</p>
      <a class="btn" href="#"><span>★</span>READ MORE<span>★</span></a>
    </li>
    <li class="vehicle">
      <div class="vehicle-photo" role="img" aria-label="Bright blue muscle car in a white studio" style="background:linear-gradient(#f4f4f4 0%,#e6e6e6 55%,#2a48c4 70%,#14278a 86%,#2e2e2e 100%)"></div>
      <h3>VEHICLE NAME</h3>
      <p>Arta libero id ullamcorper nonummy<br>nibh ligula pulvinar metus eget</p>
      <a class="btn" href="#"><span>★</span>READ MORE<span>★</span></a>
    </li>
  </ul>

  <footer class="footer">
    <svg class="footer-zig" viewBox="0 0 908 10" preserveAspectRatio="none" aria-hidden="true">
      <defs><pattern id="zigFoot" width="12" height="10" patternUnits="userSpaceOnUse"><path d="M0 10L6 2L12 10Z" fill="#f7f4c2"/></pattern></defs>
      <rect width="908" height="10" fill="url(#zigFoot)"/>
    </svg>
    <ul class="footer-nav">
      <li><a href="#">HOME</a></li>
      <li><a href="#">ABOUT</a></li>
      <li><a href="#">SERVICE</a></li>
      <li><a href="#">INVENTORY</a></li>
      <li><a href="#">SITE MAP</a></li>
      <li><a href="#">CONTACT US</a></li>
    </ul>
    <p class="copyright">© 2003-2014 Motorlane, LTD. All Rights Reserved.</p>
    <ul class="social" aria-label="Social links">
      <li></li><li></li><li></li>
    </ul>
  </footer>
</div>
</body>
</html>
```